Product Label Design

Need a product design for our Epsom salt product, needs to have a luxurious simple feel to it. The picture attached is our brand and wordage on it, the bag we think should be a stand up bag that should be offwhite/creme color. The other picture are products that we like. We updated the packaging to be a Kraft tube box, please see the attached photo for dimensions.

```html
<!DOCTYPE html>
<html lang="en">
<head>
<meta charset="utf-8">
<title>Halden Revive – Epsom Salt Tube Label</title>
<link rel="stylesheet" href="https://fonts.googleapis.com/css2?family=Open+Sans:wght@400;600;700&display=swap">
<style>
  :root {
    --page-bg: #f7f7f7;
    --label-cream: #f1efeb;
    --accent-blue: #6ccbea;
    --ink: #262626;
    --white: #ffffff;
  }
  * { box-sizing: border-box; margin: 0; padding: 0; }
  html, body {
    width: 1200px;
    height: 1200px;
    overflow: hidden;
    background: var(--page-bg);
    font-family: "Open Sans", Arial, sans-serif;
  }
  .canvas {
    position: relative;
    width: 1200px;
    height: 1200px;
  }
  .tube-label {
    position: absolute;
    left: 400px;
    top: 90px;
    width: 400px;
    height: 1010px;
    background: var(--label-cream);
    overflow: hidden;
  }
  .lid-band {
    height: 276px;
    background: var(--accent-blue);
  }
  .brand-name {
    position: absolute;
    top: 362px;
    left: 0;
    width: 100%;
    text-align: center;
    font-weight: 600;
    font-size: 84px;
    line-height: 1;
    color: var(--ink);
    letter-spacing: 1px;
  }
  .variant-band {
    position: absolute;
    top: 512px;
    left: 0;
    width: 100%;
    height: 82px;
    background: var(--accent-blue);
    display: flex;
    align-items: center;
    justify-content: center;
  }
  .variant-name {
    font-weight: 700;
    font-size: 30px;
    letter-spacing: 5px;
    color: var(--white);
  }
  .ingredients {
    position: absolute;
    top: 664px;
    left: 0;
    width: 100%;
    text-align: center;
    font-size: 17px;
    line-height: 30px;
    color: var(--ink);
  }
  .net-weight {
    position: absolute;
    top: 932px;
    left: 0;
    width: 100%;
    text-align: center;
    font-size: 14px;
    letter-spacing: 1.4px;
    color: var(--ink);
  }
</style>
</head>
<body>
<main class="canvas">
  <section class="tube-label">
    <div class="lid-band"></div>
    <h1 class="brand-name">Halden</h1>
    <div class="variant-band"><span class="variant-name">REVIVE</span></div>
    <p class="ingredients">
      US Sourced Pure Epsom Salt<br>
      (Magnesium Sulfate)<br>
      + Abies sibirica<br>
      + Fir Balsam
    </p>
    <p class="net-weight">NET WT. 3 LBS (1360 G)</p>
  </section>
</main>
</body>
</html>
```